BRIGHTWAVE PARTNERS NAMECARD

Need to design a name card with an existing logo.

As we are professional corporate services provider our name card has to project a professional image.
Should be corporate, simple & professional.

Our corporate color is maroon red but not too dull.

Please refer to our website at www.brightwavepartners.com.sg

Would attach our logo herewith.

Front surface of namecard details:
BRIGHTWAVE PARTNERS PTE LTD
Registration No. 208731945K

Lowe Hui Ting CA (Singapore)
Director

Tel +65 6481 2957
Mobile +65 9172 3806
lowe@brightwavepartners.com.sg
www.brightwavepartners.com.sg

47 Palmer Lane
#07-14 Harbourlight Plaza
Singapore 274153

Back of namecard:-
OUR CORE SERVICES
Incorporation services
Corporate Secretarial Services
Accountancy service
Goods & Services Taxation
Corporate & Personal Taxation
Financial Reporting
Payroll Administration

AFFILIATES:
TRIVANTA CORPORATE SERVICES PTE LTD
BRIGHTWAVEREGISTRYPTE LTD
ORR MANAGEMENT SERVICES PTE LTD
DW LIM AND COMPANY PTE LTD
LEDGERWISE ACADEMY

```html
<!DOCTYPE html>
<html lang="en">
<head>
<meta charset="utf-8">
<title>Brightwave Partners Stationery</title>
<link rel="stylesheet" href="https://fonts.googleapis.com/css2?family=Tinos:wght@400;700&display=swap">
<style>
  :root {
    --page: #ffffff;
    --frame: #000000;
    --paper: #ffffff;
    --ink: #1a1a1a;
    --maroon: #b0283a;
    --band: #b05a65;
    --rule: #e3c3c8;
    --on-band: #ffffff;
  }
  * { margin: 0; padding: 0; box-sizing: border-box; }
  html, body { width: 1200px; height: 1000px; overflow: hidden; background: var(--page); }
  body { position: relative; font-family: "Tinos", "Times New Roman", serif; color: var(--ink); }

  .presentation-note {
    position: absolute; left: 672px; top: 36px;
    font-size: 37px; line-height: 1; color: #000;
  }
  .mount { position: absolute; background: var(--frame); }
  .sheet { position: absolute; background: var(--paper); overflow: hidden; }

  .brand-name {
    position: absolute; color: var(--maroon); font-weight: 400;
    line-height: 1; white-space: nowrap;
  }

  .text-block { position: absolute; white-space: nowrap; }
  .text-block p + p { margin-top: 0; }

  /* envelope back */
  .env-back .brand-name { left: 94px; top: 50px; font-size: 10px; }
  .env-back .services { left: 58px; top: 78px; font-size: 6.6px; line-height: 7.6px; font-weight: 700; }
  .env-back .affiliates { left: 60px; top: 153px; font-size: 6.6px; line-height: 7.6px; }
  .flap { position: absolute; left: 0; top: 0; }

  /* envelope front */
  .env-front .brand-name { left: 16px; top: 16px; font-size: 15px; }
  .env-front .sender { left: 17px; top: 46px; font-size: 5.6px; line-height: 6.6px; }

  /* name card */
  .card .brand-name { left: 0; width: 184px; text-align: center; top: 28px; font-size: 14px; }
  .card .identity { left: 0; width: 184px; top: 50px; text-align: center; font-size: 8.6px; line-height: 10px; }
  .card .identity .gap-lg { margin-top: 21px; }
  .card .identity .gap-sm { margin-top: 9px; }
  .card .identity .gap-xs { margin-top: 8px; }
  .card .divider { position: absolute; left: 185px; top: 26px; width: 1px; height: 154px; background: var(--rule); }
  .card .services { left: 198px; top: 26px; font-size: 8.6px; line-height: 10px; }
  .card .affiliates { left: 198px; top: 120px; font-size: 8.6px; line-height: 10px; }

  /* letterhead */
  .letterhead .brand-name { left: 0; width: 100%; top: 44px; font-size: 28px; text-align: center; }
  .letterhead .rule { position: absolute; left: 30px; width: 349px; height: 1px; background: var(--rule); }
  .letterhead .col { font-size: 8.2px; line-height: 9.6px; }
  .letterhead .col .gap { display: block; height: 5px; }
  .letterhead .services-band {
    position: absolute; left: 29px; top: 485px; width: 365px; height: 113px; background: var(--band); color: var(--on-band);
  }
  .services-band .services { left: 17px; top: 12px; font-size: 8.2px; line-height: 9.6px; }
  .services-band .band-divider { position: absolute; left: 177px; top: 12px; width: 1px; height: 76px; background: rgba(255,255,255,0.25); }
  .services-band .affiliates { left: 203px; top: 12px; font-size: 8.2px; line-height: 9.6px; white-space: normal; width: 160px; }
</style>
</head>
<body>

<p class="presentation-note">presentation purposes only</p>

<!-- Envelope back -->
<div class="mount" style="left:54px; top:40px; width:498px; height:288px;"></div>
<div class="sheet env-back" style="left:96px; top:82px; width:414px; height:204px;">
  <svg class="flap" width="414" height="40" viewBox="0 0 414 40" aria-hidden="true">
    <polyline points="0,10 25,35 390,35 414,10" fill="none" stroke="#333" stroke-width="1"/>
  </svg>
  <div class="brand-name">Brightwave Partners</div>
  <div class="text-block services">
    OUR CORE SERVICES<br>Incorporation services<br>Corporate Secretarial Services<br>Accountancy service<br>
    Goods &amp; Services Taxation<br>Corporate &amp; Personal Taxation<br>Financial Reporting<br>Payroll Administration
  </div>
  <div class="text-block affiliates">
    AFFILIATES:<br>TRIVANTA CORPORATE SERVICES PTE LTD<br>BRIGHTWAVEREGISTRYPTE LTD<br>ORR MANAGEMENT SERVICES PTE LTD<br>DW LIM AND COMPANY PTE LTD<br>LEDGERWISE ACADEMY
  </div>
</div>

<!-- Envelope front -->
<div class="mount" style="left:53px; top:338px; width:498px; height:288px;"></div>
<div class="sheet env-front" style="left:91px; top:376px; width:419px; height:210px;">
  <div class="brand-name">Brightwave Partners</div>
  <div class="text-block sender">
    Lowe Hui Ting CA (Singapore)<br>Director<br><br>47 Palmer Lane<br>#07-14 Harbourlight Plaza<br>Singapore 274153
  </div>
</div>

<!-- Name card -->
<div class="mount" style="left:56px; top:652px; width:498px; height:288px;"></div>
<div class="sheet card" style="left:98px; top:693px; width:414px; height:205px;">
  <div class="brand-name">Brightwave Partners</div>
  <div class="text-block identity">
    <p>BRIGHTWAVE PARTNERS PTE LTD<br>Registration No. 208731945K</p>
    <p class="gap-lg">Lowe Hui Ting CA (Singapore)<br>Director</p>
    <p class="gap-sm">Tel +65 6481 2957<br>Mobile +65 9172 3806<br>lowe@brightwavepartners.com.sg<br>www.brightwavepartners.com.sg</p>
    <p class="gap-xs">47 Palmer Lane<br>#07-14 Harbourlight Plaza<br>Singapore 274153</p>
  </div>
  <div class="divider"></div>
  <div class="text-block services">
    OUR CORE SERVICES<br>Incorporation services<br>Corporate Secretarial Services<br>Accountancy service<br>
    Goods &amp; Services Taxation<br>Corporate &amp; Personal Taxation<br>Financial Reporting<br>Payroll Administration
  </div>
  <div class="text-block affiliates">
    AFFILIATES:<br>TRIVANTA CORPORATE SERVICES PTE LTD<br>BRIGHTWAVEREGISTRYPTE LTD<br>ORR MANAGEMENT SERVICES PTE LTD<br>DW LIM AND COMPANY PTE LTD<br>LEDGERWISE ACADEMY
  </div>
</div>

<!-- Letterhead -->
<div class="mount" style="left:626px; top:106px; width:498px; height:690px;"></div>
<div class="sheet letterhead" style="left:668px; top:148px; width:414px; height:606px;">
  <div class="brand-name">Brightwave Partners</div>
  <div class="rule" style="top:93px;"></div>
  <div class="text-block col" style="left:36px; top:105px;">
    Lowe Hui Ting CA (Singapore)<br>Director<span class="gap"></span>BRIGHTWAVE PARTNERS PTE LTD<br>Registration No. 208731945K
  </div>
  <div class="text-block col" style="left:175px; top:101px;">
    Tel +65 6481 2957<br>Mobile +65 9172 3806<br>lowe@brightwavepartners.com.sg<br>www.brightwavepartners.com.sg
  </div>
  <div class="text-block col" style="left:296px; top:105px;">
    47 Palmer Lane<br>#07-14 Harbourlight Plaza<br>Singapore 274153
  </div>
  <div class="rule" style="top:159px;"></div>

  <div class="services-band">
    <div class="text-block services">
      OUR CORE SERVICES<br>Incorporation services<br>Corporate Secretarial Services<br>Accountancy service<br>
      Goods &amp; Services Taxation<br>Corporate &amp; Personal Taxation<br>Financial Reporting<br>Payroll Administration
    </div>
    <div class="band-divider"></div>
    <div class="text-block affiliates">
      AFFILIATES:<br>TRIVANTA CORPORATE SERVICES PTE LTD<br>BRIGHTWAVEREGISTRYPTE LTD<br>ORR MANAGEMENT SERVICES PTE LTD<br>DW LIM AND COMPANY PTE LTD<br>LEDGERWISE ACADEMY
    </div>
  </div>
</div>

</body>
</html>
```